Invitation card to the opening of BRISKORA FITNESS CLUB

A successful training plan starts with BRISKORA Fitness!
Join us for our grand opening! OPEN HOUSE AND YOU ARE INVITED!
Tuesday 1st of August, 2017
Classes start from 7.30am till 9.30pm.
Explore the most fun, exciting, challenging and effective training system in the region.
Healthy drinks and delicious food will be provided.
We hope to see you there!

www.briskorafitnessclub.example
APP: BRISKORAFITNAB
Tel: 71-42 58 19

Industry/Entity Type

Fitness

Colors

Designer to choose colors to be used in the design.

Requirements
Must have
• Elegant card
Nice to have
• Logo in the background
Should not have
• pictures

```html
<!DOCTYPE html>
<html lang="en">
<head>
<meta charset="utf-8">
<title>BRISKORA Fitness Club – Grand Opening Invitation</title>
<link rel="stylesheet" href="https://fonts.googleapis.com/css2?family=Montserrat:wght@300;400;500;600;700&display=swap">
<style>
  :root {
    --silver-light: #f2f3f5;
    --silver-mid: #d6d8db;
    --silver-dark: #b9bcc0;
    --gold-light: #cbbb98;
    --gold-mid: #bcab87;
    --gold-dark: #a6977b;
    --ink: #0d0d0d;
    --stripe: #000000;
    --rule: #d3d2cf;
  }
  html, body {
    margin: 0;
    padding: 0;
    width: 1200px;
    height: 857px;
    overflow: hidden;
    background: #ffffff;
  }
  .card {
    position: relative;
    width: 1200px;
    height: 857px;
    overflow: hidden;
    font-family: "Montserrat", sans-serif;
    color: var(--ink);
  }
  .card-panels {
    position: absolute;
    inset: 0;
  }
  .text {
    position: absolute;
    margin: 0;
    line-height: 1;
    white-space: nowrap;
    text-align: center;
  }
  /* left side */
  .side-left { left: 0; width: 504px; }
  .brand-mark {
    position: absolute;
    left: 224px;
    top: 96px;
    width: 56px;
    height: 56px;
    border-radius: 50%;
    background: var(--silver-dark);
  }
  .brand-name {
    top: 172px;
    font-size: 38px;
    font-weight: 500;
    letter-spacing: 1px;
  }
  .brand-sub {
    top: 218px;
    font-size: 38px;
    font-weight: 500;
    transform: scale(0.34);
    transform-origin: center top;
    letter-spacing: 14px;
  }
  .tagline-lead {
    top: 321px;
    font-size: 50px;
    font-weight: 600;
    letter-spacing: 3px;
  }
  .tagline-mid {
    top: 390px;
    font-size: 23px;
    font-weight: 600;
    letter-spacing: 1.6px;
  }
  .tagline-name {
    top: 432px;
    font-size: 72px;
    font-weight: 500;
    letter-spacing: 2px;
  }
  .tagline-sub {
    top: 508px;
    font-size: 72px;
    font-weight: 500;
    transform: scale(0.36);
    transform-origin: center top;
    letter-spacing: 40px;
  }
  .contact-web { top: 756px; font-size: 18px; font-weight: 600; }
  .contact-app { top: 780px; font-size: 15px; font-weight: 400; }
  .contact-tel { top: 804px; font-size: 15px; font-weight: 400; }

  /* right side */
  .side-right { left: 560px; width: 616px; }
  .invite-lead {
    top: 108px;
    font-size: 44px;
    font-weight: 600;
    font-variant: small-caps;
  }
  .invite-title {
    top: 151px;
    font-size: 50px;
    font-weight: 700;
  }
  .invite-note {
    top: 247px;
    font-size: 24px;
    font-weight: 300;
  }
  .divider {
    position: absolute;
    left: 570px;
    width: 584px;
    height: 3px;
    background: var(--rule);
  }
  .divider-top { top: 302px; }
  .divider-bottom { top: 467px; }
  .event-when {
    top: 348px;
    font-size: 27px;
    font-weight: 300;
    line-height: 37px;
  }
  .event-when strong { font-weight: 600; }
  .event-about {
    top: 507px;
    font-size: 26px;
    font-weight: 300;
    line-height: 40px;
  }
  .event-food {
    top: 619px;
    font-size: 26px;
    font-weight: 300;
    line-height: 40px;
  }
  .event-close {
    top: 739px;
    font-size: 38px;
    font-weight: 600;
  }
</style>
</head>
<body>
<main class="card">
  <svg class="card-panels" width="1200" height="857" viewBox="0 0 1200 857" aria-hidden="false">
    <defs>
      <linearGradient id="silverPanel" x1="0" y1="0" x2="0.6" y2="1">
        <stop offset="0" stop-color="var(--silver-mid)"/>
        <stop offset="0.45" stop-color="var(--silver-light)"/>
        <stop offset="1" stop-color="var(--silver-dark)"/>
      </linearGradient>
      <radialGradient id="silverGlow" cx="0.45" cy="0.45" r="0.55">
        <stop offset="0" stop-color="#ffffff" stop-opacity="0.7"/>
        <stop offset="1" stop-color="#ffffff" stop-opacity="0"/>
      </radialGradient>
      <linearGradient id="goldPanel" x1="0" y1="0" x2="0.3" y2="1">
        <stop offset="0" stop-color="var(--gold-light)"/>
        <stop offset="0.5" stop-color="var(--gold-mid)"/>
        <stop offset="1" stop-color="var(--gold-dark)"/>
      </linearGradient>
    </defs>
    <g role="img" aria-label="Soft silver sparkle background with glowing light spots">
      <polygon points="0,0 564,0 448,857 0,857" fill="url(#silverPanel)"/>
      <polygon points="0,0 564,0 448,857 0,857" fill="url(#silverGlow)"/>
    </g>
    <polygon class="stripe" points="564,0 604,0 452,857 448,857" fill="var(--stripe)"/>
    <polygon class="gold-panel" points="604,0 1200,0 1200,857 452,857" fill="url(#goldPanel)"/>
  </svg>

  <section class="side-left-content">
    <span class="brand-mark" aria-hidden="true"></span>
    <p class="text side-left brand-name">BRISKORA</p>
    <p class="text side-left brand-sub">FITNESS</p>

    <p class="text side-left tagline-lead">A SUCCESSFUL</p>
    <p class="text side-left tagline-mid">TRAINING PLAN STARTS WITH</p>
    <p class="text side-left tagline-name">BRISKORA</p>
    <p class="text side-left tagline-sub">FITNESS</p>

    <p class="text side-left contact-web">www.briskorafitnessclub.example</p>
    <p class="text side-left contact-app">APP: BRISKORAFITNAB</p>
    <p class="text side-left contact-tel">TEL: 71-42 58 19</p>
  </section>

  <section class="side-right-content">
    <p class="text side-right invite-lead">Join us for our</p>
    <h1 class="text side-right invite-title">GRAND OPENING!</h1>
    <p class="text side-right invite-note">OPEN HOUSE AND YOU ARE INVITED!</p>
    <div class="divider divider-top"></div>
    <p class="text side-right event-when">Tuesday 1st of <strong>August, 2017</strong><br>Classes start from <strong>7.30am till 9.30pm.</strong></p>
    <div class="divider divider-bottom"></div>
    <p class="text side-right event-about">Explore the most fun, exciting, challenging<br>and effective training system in the region.</p>
    <p class="text side-right event-food">Healthy drinks and delicious<br>food will be provided.</p>
    <p class="text side-right event-close">WE HOPE TO SEE YOU THERE!</p>
  </section>
</main>
</body>
</html>
```